Selling my Home Flyer

I need a flyer/brochure for a house listing I am putting together. I will put all of the information together for you to include in the flyer. This will only be a front and back flyer. No extra pages and no staples will be seen. This will be printed by a large office copier, not a professional copier on standard paper. Therefore no crazy dark backgrounds with lots of bleeding colors. Pictures that I want need for sure in there are Aerial with outline, Front from left, and one of the ones showing the large yard. I included a couple sample designs that I don't hate. But feel free to get creative. I will need this on a quick turnaround and I will make comments quickly as well, so submit ASAP.

Target Market(s)

People that will by my house.

Industry/Entity Type

Real Estate Agent

Font styles to use
Serif
Sans Serif

Colors

Designer to choose colors to be used in the design.

Requirements
Must have
• The pictures I mentioned above. And the price and SF and address! I forgot to tell you the address. It is 4817 Heron Lane, Palm Beach Gardens, FL 58127.
Should not have
• Anarchy. I don't want it to look too crazy. Should be pretty straight forward.

```html
<!DOCTYPE html>
<html lang="en">
<head>
<meta charset="utf-8">
<title>4817 Heron Lane – Listing Flyer</title>
<link href="https://fonts.googleapis.com/css2?family=Hind:wght@400;500;600;700&family=Playfair+Display:wght@700;900&display=swap" rel="stylesheet">
<style>
:root{
  --orange:#f5821f;
  --ink:#1c1c1c;
  --paper:#ffffff;
  --backdrop:#d9d6d2;
  --outline:#f2ea20;
  --lawn:#4d7a32;
  --sky:#8fb9d8;
  --stucco:#e9e1cf;
}
*{box-sizing:border-box;margin:0;padding:0}
html,body{width:1200px;height:800px;overflow:hidden}
body{background:var(--backdrop);font-family:"Hind",sans-serif;color:var(--ink);position:relative}
.page{position:absolute;top:48px;width:546px;height:706px;background:var(--paper)}
.page--front{left:35px}
.page--back{left:616px}
.hero{position:absolute;left:0;top:0;width:546px;height:296px}
.hero--house{background:linear-gradient(180deg,var(--sky) 0%,#c9d8c0 30%,var(--stucco) 48%,#7f9a5a 75%,var(--lawn) 100%)}
.hero--aerial{background:linear-gradient(90deg,#3f6a2e 0%,#5a7f3a 22%,#a39480 40%,#8b7d6a 52%,#3e6b2c 70%,#6e8c4c 82%,#9a9a96 92%,#7d7d7a 100%)}
.lot-outline{position:absolute;left:0;top:0;width:546px;height:296px}
.tag{position:absolute;background:var(--orange);color:#fff}
.tag--sale{left:0;top:26px;width:225px;height:88px;font-family:"Playfair Display",serif;font-weight:700;font-size:51px;line-height:88px;padding-left:22px}
.tag--price{left:20px;top:272px;width:161px;height:37px;font-weight:700;font-size:25px;line-height:40px;text-align:center}
.tag--address{left:0;top:26px;width:224px;height:86px;font-weight:700;font-size:18.5px;line-height:23px;padding:9px 0 0 20px}
.tag--stats{left:20px;top:272px;width:363px;height:59px;font-weight:700;font-size:18.5px;line-height:23px;padding:7px 0 0 30px}
.tag--stats li{list-style:none}
.headline{position:absolute;left:20px;top:317px;width:380px;font-family:"Playfair Display",serif;font-weight:700;font-size:19.5px;line-height:24px;color:var(--orange);text-transform:uppercase}
.lead{position:absolute;left:20px;top:372px;width:350px;font-weight:600;font-size:12.2px;line-height:15.3px}
.details{position:absolute;left:20px;top:443px;width:348px;font-size:10.2px;line-height:13px}
.agent{position:absolute;left:390px;top:280px;width:150px;text-align:center}
.agent__ring{width:132px;height:132px;margin:0 auto;border-radius:50%;background:var(--paper);padding:7px}
.agent__portrait{width:118px;height:118px;border-radius:50%;background:var(--orange)}
.agent__name{font-family:"Playfair Display",serif;font-weight:700;font-size:12px;margin-top:4px;letter-spacing:.3px}
.agent__role{font-size:10px;line-height:12px}
.agent__cta{font-family:"Playfair Display",serif;font-weight:700;font-size:21px;margin-top:10px;line-height:24px}
.agent__phone{font-weight:700;font-size:20px;color:var(--orange);line-height:24px}
.section-head{position:absolute;left:20px;width:506px;display:flex;align-items:center;gap:10px;font-family:"Playfair Display",serif;font-weight:700;font-size:12px}
.section-head::before,.section-head::after{content:"";flex:1;height:2px;background:var(--orange)}
.gallery{position:absolute;left:20px;width:506px;display:flex;justify-content:space-between}
.tile{width:161px;text-align:center;font-weight:600;font-size:11.5px}
.tile__photo{width:161px;height:105px;margin-bottom:10px}
.rule{position:absolute;left:20px;width:506px;height:2px;background:var(--orange)}
.contact{position:absolute;left:20px;top:681px;width:506px;height:20px;display:flex;align-items:center;font-size:10.5px;white-space:nowrap}
.contact__intro{font-weight:600;width:219px;flex:none}
.contact__item{display:flex;align-items:center;gap:6px;flex:none;white-space:nowrap}
.contact__item--mail{width:206px}
.contact__icon{width:20px;height:20px;flex:none}
</style>
</head>
<body>

<section class="page page--front">
  <div class="hero hero--house" role="img" aria-label="Front view of two-story stucco home with tile roof, palms and landscaped lawn"></div>
  <div class="tag tag--sale">For Sale</div>
  <div class="tag tag--price">$570,000</div>

  <h1 class="headline">Pool home on coveted corner lot with oversized yard.</h1>
  <p class="lead">This impressive home boasts one of the largest yards in Palm Beach Gardens' most family friendly community, Willowmere. Enjoy the ultimate Florida lifestyle with a beautiful pool &amp; expanded patio areas - perfect for entertaining.</p>
  <p class="details">Upgraded features throughout. Custom wood and ship lap details in all bathrooms and loft. New dark wood laminate flooring upstairs. New high-efficiency A/C units with smart thermostats. New pool pump and new heater controlled from your phone! Crown molding throughout. Walk-in closets.&nbsp; Quiet &amp; private cul-de-sac.</p>

  <div class="agent">
    <div class="agent__ring"><div class="agent__portrait" role="img" aria-label="Agent portrait placeholder"></div></div>
    <p class="agent__name">DEREK MOLL</p>
    <p class="agent__role">Contact person</p>
    <p class="agent__cta">CALL TODAY</p>
    <p class="agent__phone">561-555-0142</p>
  </div>

  <h2 class="section-head" style="top:512px">EXTERIOR VIEW</h2>
  <div class="gallery" style="top:534px">
    <div class="tile"><div class="tile__photo" role="img" aria-label="Courtyard entry walkway" style="background:linear-gradient(135deg,#5f8a3c,#d8cbb0 60%,#b59a7a)"></div>COURTYARD ENTRY</div>
    <div class="tile"><div class="tile__photo" role="img" aria-label="Screened pool" style="background:linear-gradient(180deg,#3f6a33 0%,#6b7f5a 45%,#4fc4d0 70%,#b8a58a 100%)"></div>POOL</div>
    <div class="tile"><div class="tile__photo" role="img" aria-label="Patio and large yard" style="background:linear-gradient(180deg,#9cc3de 0%,#e6dcc6 40%,#b39b7c 70%,#4f8a2e 100%)"></div>PATIO AND YARD</div>
  </div>
  <div class="rule" style="top:668px"></div>
  <div class="contact">
    <span class="contact__intro">Get in touch for more information:</span>
    <span class="contact__item contact__item--mail">
      <svg class="contact__icon" viewBox="0 0 20 20"><circle cx="10" cy="10" r="10" fill="#f5821f"/><rect x="5" y="6.5" width="10" height="7" fill="none" stroke="#fff" stroke-width="1.3"/><path d="M5 6.5l5 4 5-4" fill="none" stroke="#fff" stroke-width="1.3"/></svg>
      derek@mollrealty.com</span>
    <span class="contact__item">
      <svg class="contact__icon" viewBox="0 0 20 20"><circle cx="10" cy="10" r="10" fill="#f5821f"/><path d="M5 8.5c0-2 2-3 5-3s5 1 5 3l-1.8.6-.6-1.5h-5.2l-.6 1.5z M6.5 10h7l1 4h-9z" fill="#fff"/></svg>
      561-555-0142</span>
  </div>
</section>

<section class="page page--back">
  <div class="hero hero--aerial" role="img" aria-label="Aerial view of the property and neighboring lots"></div>
  <svg class="lot-outline" viewBox="0 0 546 296"><polygon points="131,6 365,6 408,64 408,280 131,272" fill="none" stroke="#f2ea20" stroke-width="2"/></svg>
  <div class="tag tag--address">4817 Heron Lane,<br>Palm Beach Gardens,<br>FL 58127</div>
  <ul class="tag tag--stats">
    <li>• 2,307 Square Feet</li>
    <li>• 3 bedrooms and 2 ½ bathrooms</li>
  </ul>

  <h2 class="section-head" style="top:341px">INTERIOR VIEW</h2>
  <div class="gallery" style="top:364px">
    <div class="tile"><div class="tile__photo" role="img" aria-label="Kitchen" style="background:linear-gradient(180deg,#f1efe9,#d8d4cc 60%,#a9a49a)"></div>KITCHEN</div>
    <div class="tile"><div class="tile__photo" role="img" aria-label="Master bedroom" style="background:linear-gradient(180deg,#ece6d6,#d9cfb8 55%,#7a4a2e)"></div>MASTER BEDROOM</div>
    <div class="tile"><div class="tile__photo" role="img" aria-label="Master bathroom" style="background:linear-gradient(135deg,#c9b79c,#ebe5da 55%,#d8c9b0)"></div>MASTER BATHROOM</div>
  </div>
  <div class="rule" style="top:499px"></div>

  <h2 class="section-head" style="top:512px">INTERIOR VIEW</h2>
  <div class="gallery" style="top:534px">
    <div class="tile"><div class="tile__photo" role="img" aria-label="Dining room" style="background:linear-gradient(180deg,#efe8da,#d9cbb2 55%,#7d5b3e)"></div>DINING ROOM</div>
    <div class="tile"><div class="tile__photo" role="img" aria-label="Loft" style="background:linear-gradient(180deg,#e9dcc0,#efe7d6 55%,#5a3a24)"></div>LOFT</div>
    <div class="tile"><div class="tile__photo" role="img" aria-label="Powder room" style="background:linear-gradient(180deg,#dcd8d1,#b9b3aa 55%,#5b5a5a)"></div>POWDER ROOM</div>
  </div>
  <div class="rule" style="top:668px"></div>
  <div class="contact">
    <span class="contact__intro">Get in touch for more information:</span>
    <span class="contact__item contact__item--mail">
      <svg class="contact__icon" viewBox="0 0 20 20"><circle cx="10" cy="10" r="10" fill="#f5821f"/><rect x="5" y="6.5" width="10" height="7" fill="none" stroke="#fff" stroke-width="1.3"/><path d="M5 6.5l5 4 5-4" fill="none" stroke="#fff" stroke-width="1.3"/></svg>
      derek@mollrealty.com</span>
    <span class="contact__item">
      <svg class="contact__icon" viewBox="0 0 20 20"><circle cx="10" cy="10" r="10" fill="#f5821f"/><path d="M5 8.5c0-2 2-3 5-3s5 1 5 3l-1.8.6-.6-1.5h-5.2l-.6 1.5z M6.5 10h7l1 4h-9z" fill="#fff"/></svg>
      561-555-0142</span>
  </div>
</section>

</body>
</html>
```